Corvane Photography Business Card Design

I need a business card designed for a photography business based in Perth, Western Australia called Corvane Photography.

We specialise in wedding, event photography and portrait photography.

The business card must borrow the style of the attached logo.

The hex codes for the colours in the logo are:
#ED1D85 - Pink
#89C23E - Green
#37282F - Black

The name on the card will be:
Name: Teodric
Phone: 0417360825
Website: www.corvanephotography-example.com.au
Facebook: corvanephotography

I am open and happy to accept creative concepts.

Industry/Entity Type

Business

```html
<!DOCTYPE html>
<html lang="en">
<head>
<meta charset="utf-8">
<title>Corvane Photography – Business Card</title>
<link rel="stylesheet" href="https://fonts.googleapis.com/css2?family=Questrial&family=Open+Sans:wght@400&family=Cinzel:wght@600&display=swap">
<style>
  :root {
    --pink: #ED1D85;
    --green: #89C23E;
    --ink: #37282F;
    --band: #463a3e;
    --paper: #ffffff;
    --backdrop: #c9ab82;
    --text: #3d3d3d;
    --faint-pink: #fbe3ec;
  }
  * { margin: 0; padding: 0; box-sizing: border-box; }
  html, body { width: 1196px; height: 1200px; overflow: hidden; }
  body { background: var(--backdrop); position: relative; }

  .card {
    position: absolute;
    left: 174px;
    width: 852px;
    height: 488px;
    background: var(--paper);
    border-radius: 30px;
    overflow: hidden;
  }
  .card--front { top: 102px; }
  .card--back { top: 628px; border: 1.5px solid var(--ink); }

  .brand-mark {
    position: absolute;
    left: 330px;
    top: 150px;
    display: flex;
    align-items: center;
    gap: 12px;
    font-family: "Questrial", sans-serif;
    font-size: 22px;
    color: var(--pink);
    letter-spacing: 2px;
  }
  .brand-mark__dot {
    width: 22px; height: 22px; border-radius: 50%;
    background: var(--green);
  }

  .studio-title {
    position: absolute;
    font-family: "Questrial", sans-serif;
    color: var(--ink);
    text-transform: uppercase;
    white-space: nowrap;
  }
  .card--front .studio-title {
    left: 36px; top: 200px;
    font-size: 20px;
    letter-spacing: 9.4px;
  }

  .contact-list {
    position: absolute;
    left: 36px; top: 278px;
    list-style: none;
    font-family: "Open Sans", sans-serif;
    font-size: 20px;
    color: var(--text);
  }
  .contact-list li {
    display: flex; align-items: center; gap: 8px;
    height: 44px;
  }
  .contact-list svg { flex: none; }
  .social-square {
    width: 18px; height: 18px; background: #3b5a98; border-radius: 3px;
    margin-right: 4px;
  }

  .wave { position: absolute; left: 0; top: 0; }

  .holder-name {
    position: absolute;
    right: 56px; top: 420px;
    font-family: "Cinzel", serif;
    font-weight: 600;
    font-size: 36px;
    letter-spacing: 2px;
    color: var(--paper);
  }

  .back-circle {
    position: absolute;
    left: 236px; top: 40px;
    width: 380px; height: 380px;
    border-radius: 50%;
    background: var(--faint-pink);
  }
  .card--back .studio-title {
    left: 0; right: 0; top: 224px;
    text-align: center;
    font-size: 25px;
    letter-spacing: 13.5px;
    padding-left: 13px;
  }
</style>
</head>
<body>

<section class="card card--front" aria-label="Business card front">
  <div class="brand-mark"><span class="brand-mark__dot"></span>Corvane Photography</div>

  <h1 class="studio-title">Corvane Photography</h1>

  <ul class="contact-list">
    <li>
      <svg width="18" height="18" viewBox="0 0 18 18" aria-hidden="true">
        <circle cx="9" cy="9" r="8" fill="none" stroke="#3d3d3d" stroke-width="1.4"/>
        <path d="M6 5c-1 2 0 5 3 7l1.5-1.5-1.5-1.5-1 .5c-.6-.6-1-1.3-1.2-2l.9-.8L7 5z" fill="#3d3d3d"/>
      </svg>
      <span>0417360825</span>
    </li>
    <li>
      <svg width="18" height="18" viewBox="0 0 18 18" aria-hidden="true">
        <circle cx="9" cy="9" r="7.5" fill="none" stroke="#3d3d3d" stroke-width="1.3"/>
        <ellipse cx="9" cy="9" rx="3.2" ry="7.5" fill="none" stroke="#3d3d3d" stroke-width="1.1"/>
        <line x1="1.5" y1="9" x2="16.5" y2="9" stroke="#3d3d3d" stroke-width="1.1"/>
        <line x1="3" y1="5" x2="15" y2="5" stroke="#3d3d3d" stroke-width="1"/>
        <line x1="3" y1="13" x2="15" y2="13" stroke="#3d3d3d" stroke-width="1"/>
      </svg>
      <span>www.corvanephotography-example.com.au</span>
    </li>
    <li>
      <span class="social-square" aria-hidden="true"></span>
      <span>corvanephotography</span>
    </li>
  </ul>

  <svg class="wave" width="852" height="488" viewBox="0 0 852 488" aria-hidden="true">
    <path d="M0 426 C 120 452, 220 466, 320 460 C 500 448, 680 380, 852 412 L852 488 L0 488 Z" fill="var(--band)"/>
    <path d="M0 404 C 120 440, 220 458, 320 452 C 500 440, 680 360, 852 392 L852 404 C 680 374, 500 452, 320 460 C 220 466, 120 448, 0 416 Z" fill="var(--pink)"/>
  </svg>

  <div class="holder-name">Teodric</div>
</section>

<section class="card card--back" aria-label="Business card back">
  <div class="back-circle" aria-hidden="true"></div>
  <h2 class="studio-title">Corvane Photography</h2>
</section>

</body>
</html>
```